New wine label design needed for exciting new wine business

A wine label design is required for a new wine production business based in Australia. This label will need to incorporate the business name 'Oleno-Cru'. We would like it to have a classic feel for a super premium wine and to reflect prestige. Colour suggestions may include a white background and the use of the colour red although we are open to any colors. This label must reflect a serious wine at a serious price. We want our design to attract attention and have a relevance that will stand the test of time!

Thanks to everyone who provided designs for our wine label. We have been very impressed by the calibre of designs! We will be making a decision very soon.

```html
<!DOCTYPE html>
<html lang="en">
<head>
<meta charset="utf-8">
<title>Oleno-Cru Wine Labels</title>
<link rel="stylesheet" href="https://fonts.googleapis.com/css2?family=Questrial&family=Cormorant+Garamond:wght@500&display=swap">
<style>
  :root {
    --page: #ffffff;
    --band: #ffffff;
    --chard-dark: #b9780f;
    --chard-mid: #d59a1e;
    --chard-light: #e5b643;
    --chard-ink: #6b3f06;
    --chard-faint: rgba(255, 214, 110, 0.55);
    --cab-dark: #240305;
    --cab-mid: #2f0a0d;
    --cab-light: #4a2c30;
    --cab-ink: #4b0a0c;
    --cab-faint: rgba(200, 170, 172, 0.35);
    --cab-pointer: #2b2b2b;
    --sub-ink: #3a3a3a;
  }
  html, body {
    margin: 0;
    padding: 0;
    width: 872px;
    height: 1200px;
    overflow: hidden;
    background: var(--page);
  }
  .canvas {
    position: relative;
    width: 872px;
    height: 1200px;
  }
  .label {
    position: absolute;
    top: 478px;
    width: 226px;
    height: 506px;
  }
  .label--chardonnay { left: 146px; }
  .label--cabernet { left: 512px; }

  .panel {
    position: absolute;
    left: 0;
    width: 100%;
  }
  .panel--upper { top: 0; height: 159px; }
  .panel--lower { top: 244px; height: 262px; }

  .label--chardonnay .panel {
    background: linear-gradient(90deg, var(--chard-dark) 0%, var(--chard-mid) 55%, var(--chard-light) 100%);
  }
  .label--cabernet .panel {
    background: linear-gradient(90deg, var(--cab-dark) 0%, var(--cab-mid) 55%, var(--cab-light) 100%);
  }

  .faint-name {
    position: absolute;
    top: 62px;
    left: 0;
    width: 100%;
    text-align: center;
    font-family: "Cormorant Garamond", serif;
    font-weight: 500;
    font-size: 34px;
    letter-spacing: 2px;
  }
  .label--chardonnay .faint-name { color: var(--chard-faint); }
  .label--cabernet .faint-name { color: var(--cab-faint); }

  .band {
    position: absolute;
    top: 159px;
    left: 0;
    width: 100%;
    height: 85px;
    background: var(--band);
    text-align: center;
  }
  .pointer {
    position: absolute;
    left: 104px;
    width: 18px;
    height: 15px;
  }
  .pointer--down { top: 0; }
  .pointer--up { bottom: 0; }

  .varietal {
    margin: 30px 0 0;
    font-family: "Questrial", sans-serif;
    font-size: 12.5px;
    letter-spacing: 0.3px;
    line-height: 1;
  }
  .label--chardonnay .varietal { color: var(--chard-ink); }
  .label--cabernet .varietal { color: var(--cab-ink); }

  .region {
    margin: 5px 0 0;
    font-family: "Cormorant Garamond", serif;
    font-weight: 500;
    font-size: 7px;
    letter-spacing: 1px;
    color: var(--sub-ink);
    line-height: 1;
  }

  .maker {
    position: absolute;
    top: 102px;
    left: 0;
    width: 100%;
    text-align: center;
    font-family: "Cormorant Garamond", serif;
    font-weight: 500;
  }
  .maker-name {
    margin: 0;
    font-size: 12px;
    letter-spacing: 0.6px;
    line-height: 1;
  }
  .maker-tagline {
    margin: 5px 0 0;
    font-size: 6.5px;
    letter-spacing: 1.2px;
    line-height: 1;
  }
  .label--chardonnay .maker { color: var(--chard-ink); }
  .label--cabernet .maker { color: #c9b2b4; }
</style>
</head>
<body>
<main class="canvas">

  <section class="label label--chardonnay" aria-label="Chardonnay label">
    <div class="panel panel--upper">
      <span class="faint-name">OLENO-CRU</span>
    </div>
    <div class="band">
      <svg class="pointer pointer--down" viewBox="0 0 18 15" aria-hidden="true"><polygon points="0,0 18,0 9,15" fill="var(--chard-mid)"/></svg>
      <h2 class="varietal">CHARDONNAY</h2>
      <p class="region">COONAWARRA, SOUTH AUSTRALIA</p>
      <svg class="pointer pointer--up" viewBox="0 0 18 15" aria-hidden="true"><polygon points="9,0 18,15 0,15" fill="var(--chard-mid)"/></svg>
    </div>
    <div class="panel panel--lower">
      <div class="maker">
        <p class="maker-name">OLENO-CRU</p>
        <p class="maker-tagline">WORLD ACCLAIMED WINEMAKERS</p>
      </div>
    </div>
  </section>

  <section class="label label--cabernet" aria-label="Cabernet Sauvignon label">
    <div class="panel panel--upper">
      <span class="faint-name">OLENO-CRU</span>
    </div>
    <div class="band">
      <svg class="pointer pointer--down" viewBox="0 0 18 15" aria-hidden="true"><polygon points="0,0 18,0 9,15" fill="var(--cab-pointer)"/></svg>
      <h2 class="varietal">CABERNET SAUVIGNON</h2>
      <p class="region">COONAWARRA, SOUTH AUSTRALIA</p>
      <svg class="pointer pointer--up" viewBox="0 0 18 15" aria-hidden="true"><polygon points="9,0 18,15 0,15" fill="var(--cab-pointer)"/></svg>
    </div>
    <div class="panel panel--lower">
      <div class="maker">
        <p class="maker-name">OLENO-CRU</p>
        <p class="maker-tagline">WORLD ACCLAIMED WINEMAKERS</p>
      </div>
    </div>
  </section>

</main>
</body>
</html>
```